Let's help people Orlanta with better hearing!

I need a business card for my private practice. I am a Dr. of Audiology and focus on hearing and tinnitus (ringing in the ears) treatment. My practice is named "Orlanta Hearing and Tinnitus Solutions". I want to communicate the idea of improved quality of life utilizing a natural color pallet Love the color turquoise as an accent. Want a professional look, while eye catching. I'm open to nontraditional design aesthetic. Something to get excited about and motivate people to improve their lives!

```html
<!DOCTYPE html>
<html lang="en">
<head>
<meta charset="utf-8">
<title>Orlanta Hearing &amp; Tinnitus Solutions – Business Card</title>
<link rel="stylesheet" href="https://fonts.googleapis.com/css2?family=Questrial&family=Montserrat:wght@600&display=swap">
<style>
  :root {
    --turquoise: #14b1a4;
    --turquoise-soft: #5cc7b8;
    --cream: #f4ecd3;
    --mint: #cde9da;
    --white: #ffffff;
    --backdrop: #e6e7e8;
  }
  * { box-sizing: border-box; margin: 0; padding: 0; }
  html, body {
    width: 1200px;
    height: 900px;
    overflow: hidden;
    background: var(--backdrop);
  }
  .canvas {
    position: relative;
    width: 1200px;
    height: 900px;
  }
  .card {
    position: absolute;
    width: 560px;
    height: 320px;
    border-radius: 4px;
    overflow: hidden;
    box-shadow: 0 10px 28px rgba(0,0,0,0.14);
  }
  .card--back { left: 580px; top: 90px; }
  .card--front { left: 60px; top: 470px; }

  .card__pattern {
    position: absolute;
    inset: 0;
    background: linear-gradient(135deg, var(--turquoise-soft) 0%, var(--mint) 45%, var(--cream) 70%, var(--turquoise-soft) 100%);
  }
  .card__disc {
    position: absolute;
    left: 50%;
    top: 50%;
    width: 236px;
    height: 236px;
    transform: translate(-50%, -50%);
    border-radius: 50%;
    background: var(--turquoise);
    display: flex;
    flex-direction: column;
    align-items: center;
    justify-content: center;
    color: var(--white);
    text-align: center;
    font-family: "Questrial", sans-serif;
  }

  /* Front: practice name */
  .brand__name {
    font-weight: 400;
    font-size: 44px;
    line-height: 1;
    letter-spacing: 1px;
  }
  .brand__rule {
    display: block;
    width: 190px;
    height: 1px;
    background: var(--white);
    margin: 8px 0 6px;
  }
  .brand__tagline {
    font-size: 15px;
    line-height: 1.2;
    letter-spacing: 0.6px;
    text-transform: uppercase;
  }

  /* Back: contact details */
  .contact__name {
    font-family: "Montserrat", sans-serif;
    font-weight: 600;
    font-size: 13px;
    line-height: 1.2;
  }
  .contact__title {
    font-size: 12.5px;
    line-height: 1.2;
  }
  .contact__phone {
    font-family: "Montserrat", sans-serif;
    font-weight: 600;
    font-size: 12px;
    margin-top: 9px;
  }
  .contact__web {
    font-size: 11px;
    line-height: 1.2;
    margin-top: 3px;
  }
  .contact__address {
    font-size: 9.5px;
    line-height: 1.25;
    margin-top: 8px;
  }
</style>
</head>
<body>
<main class="canvas">

  <section class="card card--back" aria-label="Business card back">
    <div class="card__pattern" role="img" aria-label="Decorative concentric ring pattern in turquoise, cream and gold"></div>
    <div class="card__disc">
      <p class="contact__name">Marla Vence</p>
      <p class="contact__title">AuD, CCC-A</p>
      <p class="contact__title">Doctor of Audiology</p>
      <p class="contact__phone">(555) 014-2270</p>
      <p class="contact__web">hello@orlantahearing.com<br>www.orlantahearing.com</p>
      <p class="contact__address">1200 Meadow Rd<br>Suite 210<br>Fairview, TN 37062</p>
    </div>
  </section>

  <section class="card card--front" aria-label="Business card front">
    <div class="card__pattern" role="img" aria-label="Decorative concentric ring pattern in turquoise, cream and gold"></div>
    <div class="card__disc">
      <h1 class="brand__name">Orlanta</h1>
      <span class="brand__rule"></span>
      <p class="brand__tagline">Hearing &amp; Tinnitus<br>Solutions</p>
      <span class="brand__rule"></span>
    </div>
  </section>

</main>
</body>
</html>
```